"Breathe & Bloom" Book Cover 5.5x8.5

Title of the book is "Breathe & Bloom"
Subtitle is "Unmasking Pricing Myths"
I've used PixelGuild on multiple occasions you can look on my Borvex page, Mark Delwitt, to see the covers I've used in the other projects I've done.
The target audience are people who have been tricked to think they can't retire because inflation, i.e. cost of living is going up so much they must work to keep up. There is no evidence of this.
And those are the people I want to reach so they can "Breathe...and Bloom."
Target Market(s)
Americans aged 55 and over who are thinking about retirement
Industry/Entity Type
Financial
Requirements
Nice to have
- Keep It Simple, Stupid is my mantra. Just make it pop out when people are browsing
Should not have
- No piggy banks. No old people sitting on a beach.

```html
<!DOCTYPE html>
<html lang="en">
<head>
<meta charset="utf-8">
<title>Breathe &amp; Bloom — Book Cover</title>
<link href="https://fonts.googleapis.com/css2?family=Passion+One:wght@700&family=Open+Sans:ital,wght@0,400;1,700&display=swap" rel="stylesheet">
<style>
  :root {
    --green: #006934;
    --black: #0a0a0c;
    --yellow: #f6c300;
    --white: #ffffff;
    --dock: #5a4130;
    --sky: #e9e2c2;
    --water: #2f7a5c;
    --water-deep: #1f6a48;
  }
  html, body {
    margin: 0;
    padding: 0;
    width: 776px;
    height: 1200px;
    overflow: hidden;
    background: var(--white);
  }
  .cover {
    position: relative;
    width: 776px;
    height: 1200px;
    overflow: hidden;
  }
  .cover-scene {
    position: absolute;
    inset: 0;
    background: linear-gradient(180deg,
      #3b2a22 0%,
      var(--dock) 14%,
      #6b5a48 30%,
      #a49273 44%,
      var(--sky) 56%,
      #cfc6a0 63%,
      #7fa58a 70%,
      var(--water) 80%,
      var(--water-deep) 100%);
  }
  .title {
    position: absolute;
    left: 0;
    top: 0;
    width: 776px;
    height: 500px;
  }
  .title text {
    font-family: "Passion One", "Arial Black", sans-serif;
    font-weight: 700;
  }
  .subtitle-band {
    position: absolute;
    left: 0;
    top: 518px;
    width: 776px;
    height: 70px;
    background: var(--green);
  }
  .subtitle {
    margin: 0;
    position: absolute;
    left: 63px;
    top: 9px;
    font-family: "Open Sans", Arial, sans-serif;
    font-style: italic;
    font-weight: 700;
    font-size: 33px;
    line-height: 50px;
    color: var(--white);
  }
  .author {
    position: absolute;
    left: 0;
    width: 776px;
    top: 1068px;
    margin: 0;
    text-align: center;
    font-family: "Open Sans", Arial, sans-serif;
    font-weight: 400;
    font-size: 86px;
    line-height: 100px;
    color: var(--white);
    letter-spacing: 1px;
  }
</style>
</head>
<body>
  <main class="cover">
    <div class="cover-scene" role="img" aria-label="Photo: bare feet dangling from a wooden dock over calm green sea water at sunset"></div>

    <svg class="title" viewBox="0 0 776 500" aria-label="Breathe &amp; Bloom">
      <text x="75" y="328" font-size="150" textLength="395" lengthAdjust="spacingAndGlyphs"
            fill="var(--green)" stroke="var(--white)" stroke-width="8" stroke-linejoin="round" paint-order="stroke">BREATHE</text>
      <rect x="483" y="214" width="108" height="119" fill="var(--yellow)"/>
      <text x="537" y="318" font-size="130" text-anchor="middle" fill="#1c1c1e">&amp;</text>
      <text x="70" y="487" font-size="200" textLength="565" lengthAdjust="spacingAndGlyphs"
            fill="var(--black)" stroke="var(--white)" stroke-width="8" stroke-linejoin="round" paint-order="stroke">BLOOM</text>
    </svg>

    <div class="subtitle-band">
      <p class="subtitle">Unmasking Pricing Myths</p>
    </div>

    <p class="author">Mark Delwitt</p>
  </main>
</body>
</html>
```